Einladungskarte
Zielgruppe
Hochzeitsgäste zwischen 30 und 40
Aufgabenstellung
Die Einladung hat folgende Eckdaten:
- Format Din A5 (Doppelseitiger DinA 4 gefalzt) Einladungsbogen (wird leichter Karton)
- Zusätzlicher Einlagebogen für Einladungstext
- Stil klassisch/elegant eher schlicht aber jung
- Grundthema Gerberablume (weiß, beige, rot oder orange)
- Hintergrund (hell)
- Zusätzlich zur Einladung wird Bildrecht der Blume für ein Banner auf der Hochzeitswebseite benötigt
- Editierbare Graphikdatei wird benötigt (da der Text der Einladung noch nicht final ist)

```html
<!DOCTYPE html>
<html lang="de">
<head>
<meta charset="utf-8">
<title>Einladung zur Hochzeit – Lena &amp; Jonas</title>
<link rel="stylesheet" href="https://fonts.googleapis.com/css2?family=Great+Vibes&display=swap">
<style>
  :root {
    --paper: #f9f5ec;
    --wine: #9b1718;
    --rose: #d9a39c;
    --rose-soft: #eed3cc;
    --white: #ffffff;
  }
  html, body {
    margin: 0;
    padding: 0;
    overflow: hidden;
    background: var(--paper);
  }
  .card {
    position: relative;
    width: 849px;
    height: 1200px;
    background: var(--paper);
    overflow: hidden;
  }
  .frame-lines {
    position: absolute;
    inset: 0;
  }
  .flower-ornament {
    position: absolute;
    left: 0;
    top: 0;
    width: 320px;
    height: 660px;
    border-bottom-right-radius: 300px 360px;
    border-top-right-radius: 120px 60px;
    background:
      radial-gradient(circle at 70px 310px, var(--rose) 0%, rgba(217, 163, 156, 0.55) 30%, rgba(238, 211, 204, 0) 55%),
      radial-gradient(circle at 140px 40px, rgba(217, 163, 156, 0.8) 0%, rgba(238, 211, 204, 0) 30%),
      radial-gradient(circle at 240px 240px, rgba(217, 163, 156, 0.75) 0%, rgba(238, 211, 204, 0) 28%),
      radial-gradient(circle at 185px 515px, rgba(217, 163, 156, 0.75) 0%, rgba(238, 211, 204, 0) 25%),
      var(--rose-soft);
  }
  .title-band {
    position: absolute;
    left: 0;
    top: 871px;
    width: 849px;
    height: 124px;
    background: var(--wine);
  }
  .title {
    position: absolute;
    left: 36px;
    top: 880px;
    margin: 0;
    font-family: "Great Vibes", cursive;
    font-weight: 400;
    font-size: 70px;
    line-height: 1.3;
    letter-spacing: 1.5px;
    color: var(--white);
    white-space: nowrap;
  }
  .couple {
    position: absolute;
    left: 372px;
    top: 1000px;
    margin: 0;
    font-family: "Great Vibes", cursive;
    font-weight: 400;
    font-size: 74px;
    line-height: 1.3;
    letter-spacing: 2px;
    color: var(--wine);
    white-space: nowrap;
  }
</style>
</head>
<body>
  <main class="card">
    <div class="flower-ornament" role="img" aria-label="Gerbera-Blumenranke in Weinrot als Eckornament"></div>

    <svg class="frame-lines" width="849" height="1200" viewBox="0 0 849 1200" aria-hidden="true">
      <g stroke="var(--wine)" stroke-width="2" fill="none">
        <line x1="221" y1="29" x2="832" y2="29"/>
        <line x1="221" y1="56" x2="832" y2="56"/>
        <line x1="791" y1="0" x2="791" y2="1200"/>
        <line x1="818" y1="0" x2="818" y2="1200"/>
      </g>
      <rect class="heart-box" x="791" y="29" width="27" height="27" fill="var(--wine)"/>
      <path class="heart" d="M804.5 48 C797 43 797 36.5 801 36 C803 35.8 804 37 804.5 38.5 C805 37 806 35.8 808 36 C812 36.5 812 43 804.5 48 Z" fill="var(--white)"/>
    </svg>

    <div class="title-band"></div>
    <h1 class="title">Einladung zur Hochzeit</h1>
    <p class="couple">Lena &amp; Jonas</p>
  </main>
</body>
</html>
```